Business Card Design Project

We consult with hotels on setting rates and maximizing a revenue strategy

Industry/Entity Type

Business

Contact Information for Business Card

I am not sure what I want. Our company offers high level consulting to hotels around the country but we are also laid back. I would like something that is professional but also shows the laid back side

```html
<!DOCTYPE html>
<html lang="en">
<head>
<meta charset="utf-8">
<title>Rivermark Business Card</title>
<link href="https://fonts.googleapis.com/css2?family=Saira:wght@600&family=Source+Sans+3:wght@300;400;700&display=swap" rel="stylesheet">
<style>
  :root {
    --backdrop: #a3a5a5;
    --paper: #ffffff;
    --ink: #161616;
    --ink-soft: #2a2a2a;
    --teal: #2a8a82;
    --teal-dark: #1f6e68;
    --brown: #2e2420;
    --rule: #8a8a8a;
  }
  * { margin: 0; padding: 0; box-sizing: border-box; }
  html, body { width: 1200px; height: 1200px; overflow: hidden; }
  body {
    position: relative;
    background: var(--backdrop);
    font-family: "Source Sans 3", sans-serif;
    color: var(--ink);
  }
  .card { position: absolute; width: 840px; height: 480px; overflow: hidden; }

  /* Front */
  .card-front { left: 46px; top: 55px; background: var(--paper); }
  .brand-mark {
    position: absolute; left: 232px; top: 152px;
    width: 40px; height: 40px; background: var(--teal);
  }
  .brand-name {
    position: absolute; left: 282px; top: 144px;
    font-family: "Saira", sans-serif; font-weight: 600;
    font-size: 34px; line-height: 40px; letter-spacing: 1px;
    color: var(--ink-soft);
  }
  .brand-tagline {
    position: absolute; left: 364px; top: 180px;
    width: 220px; height: 20px; background: var(--brown);
    color: #fff; font-weight: 700; font-size: 13px; line-height: 20px;
    text-align: center;
  }
  .brand-web {
    position: absolute; left: 276px; top: 201px; width: 350px;
    font-size: 19px; letter-spacing: 3.2px; color: var(--ink);
    text-align: center;
  }
  .person { position: absolute; left: 92px; top: 254px; }
  .person-name { font-size: 29px; font-weight: 300; line-height: 36px; white-space: nowrap; }
  .person-name strong { font-weight: 700; font-size: 36px; }
  .person-role { margin-left: 52px; font-size: 18px; line-height: 22px; white-space: nowrap; }
  .divider {
    position: absolute; left: 420px; top: 229px;
    width: 1px; height: 178px; background: var(--rule);
  }
  .contact-icons { position: absolute; left: 467px; top: 249px; }
  .contact-list { position: absolute; left: 528px; top: 246px; list-style: none; }
  .contact-list li { height: 42px; font-size: 20px; font-weight: 300; line-height: 32px; }
  .contact-list li.email { font-size: 16px; letter-spacing: 0.6px; font-weight: 400; }

  /* Back */
  .card-back { left: 307px; top: 627px; }
  .back-field {
    position: absolute; inset: 0;
    background:
      radial-gradient(ellipse 420px 300px at 470px 420px, rgba(80,225,210,0.9), rgba(20,190,170,0) 70%),
      linear-gradient(90deg, #041614 0%, #06403a 25%, #0b8a7e 50%, #16b3a2 65%, #1a8a7c 85%, #4f7a78 100%);
  }
  .back-name {
    position: absolute; left: 200px; top: 180px; width: 432px;
    font-family: "Saira", sans-serif; font-weight: 600;
    font-size: 66px; line-height: 64px; letter-spacing: 1px;
    color: #050505; text-align: center;
  }
  .back-tagline {
    position: absolute; left: 202px; top: 243px;
    width: 429px; height: 38px; background: #000;
    color: #fff; font-weight: 700; font-size: 26px; line-height: 38px;
    letter-spacing: 1px; text-align: center;
  }
  .back-web {
    position: absolute; left: 160px; top: 284px; width: 510px;
    font-weight: 700; font-size: 19px; letter-spacing: 13.5px;
    color: #050505; text-align: center;
  }
</style>
</head>
<body>

<section class="card card-front">
  <div class="brand-mark"></div>
  <div class="brand-name">RIVERMARK</div>
  <div class="brand-tagline">Revenue Management Solutions</div>
  <div class="brand-web">www.RivermarkRMS.com</div>

  <div class="person">
    <div class="person-name">Nora <strong>Whitfield</strong></div>
    <div class="person-role">Regional Revenue Manager</div>
  </div>

  <div class="divider"></div>

  <svg class="contact-icons" width="30" height="116" viewBox="0 0 30 116" aria-hidden="true">
    <g fill="none" stroke="var(--teal)" stroke-width="1.5">
      <line x1="15" y1="27" x2="15" y2="43"/>
      <line x1="15" y1="70" x2="15" y2="86"/>
      <circle cx="15" cy="14" r="12.5"/>
      <circle cx="15" cy="56" r="12.5"/>
      <circle cx="15" cy="98" r="12.5"/>
    </g>
    <path d="M10 8 l3 -1 2 4 -2 1.5 q1 3.5 4 5 l1.5 -2 4 2 -1 3 q-7 0 -11.5 -12.5z" fill="var(--teal-dark)"/>
    <g fill="var(--teal-dark)">
      <rect x="8" y="51" width="14" height="4" rx="1"/>
      <rect x="9" y="55" width="12" height="7" rx="1"/>
      <rect x="11" y="57" width="8" height="1.5" fill="#fff"/>
    </g>
    <g fill="none" stroke="var(--teal-dark)" stroke-width="1.4">
      <rect x="8" y="93" width="14" height="10"/>
      <polyline points="8,93 15,99 22,93"/>
    </g>
  </svg>

  <ul class="contact-list">
    <li>1 (555) 014-0055</li>
    <li>1 (555) 014-1875</li>
    <li class="email">nora@rivermarkRMS.com</li>
  </ul>
</section>

<section class="card card-back">
  <div class="back-field" role="img" aria-label="Teal mosaic gradient background with a faint bridge illustration"></div>
  <div class="back-name">RIVERMARK</div>
  <div class="back-tagline">Revenue Managment Solution</div>
  <div class="back-web">www.RivermarkRMS.com</div>
</section>

</body>
</html>
```